Wordpress design for my private practice website - Psychotherapist

I would like a simple, clean, and elegant design for my private practice website. I work with both adults and children so I'd like it to appeal to both. However, since parents make the choice as to where to send their child for therapy, I want it to appeal to adults more. I would like the pictures on the site to have a calming effect - maybe using sand and water and rocks. I am attaching files with my company logo. I would also like my name incorporated into the header - Colette Brannigan, LCSW, Registered Play Therapist. I've also uploaded a picture of myself for my About Page.

I like the design of these 2 website and want something similar:
www.drlorapenwick.example
www.harwood-tallis.example

I would like a home page that highlights a calming graphic across the entire top of the page as well as my practice logo and my name.

I'd like a link to social media sites on the top of the homepage - facebook, pinterest.

I want a simple bar across the top with the following tabs:
Home
About Me (subtabs Who I Am, Specialties and Approach)
Counseling Services (subtabs Individual Counseling, Play Therapy, Sandplay Therapy,)
Fees
FAQs
Contact Me (would love this to be a fill in the blank contact form that sends info to my email address - should include name, phone number, email and a comment box for more information requested)
Blog (this will link with another wordpress blog)

Target Market(s)

Parents of children under age 12 with behavioral problems or are dealing with the breakup of their family through divorce - looking for someone to work with their young child. I also work with Adults that are overwhelmed and worried - often women that have many life stressors and are feeling burnt out on life and meeting everyone's needs. Families going through some type of trauma, including divorce or grief work. I also work with individuals going through a transition of religious beliefs - often exiting the religion of their youth and undergoing a crisis of faith at midlife.

Industry/Entity Type

Mental Health

Contact Information for Business Card

Colette Brannigan, LCSW
Registered Play Therapist
4917 Wexmoor Lane
Idaho Falls, Idaho 83404
(208)555-0187
www.stillbrookcounseling.example

On the opposite side, I'd like an appointment reminder area - with the following text:

Your next appointment is
_____/______/______ at ______am/pm
Please give 24 hrs notice if you need to cancel your appointment.

Coding

Coded - Design and coding required

Number of Pages Required

5+ page

Font styles to use
Sans Serif

Colors
33a6d7
9bcb3c
0355a3

Requirements
Must have
• I'd like it to be a wordpress site. I'm such a newby at web design - but I need to be able to add content and manage the site myself once it is up and running.
Nice to have
• I like the design of these 2 websites and want something similar:
• www.drlorapenwick.example
• www.harwood-tallis.example
• They are clean, easy to navigate and calming.
Should not have
• Should not look like a childcare website.

```html
<!DOCTYPE html>
<html lang="en">
<head>
<meta charset="utf-8">
<title>Stillbrook Counseling – Home</title>
<link rel="stylesheet" href="https://fonts.googleapis.com/css2?family=PT+Sans:ital,wght@0,400;0,700;1,400;1,700&display=swap">
<style>
:root{
  --brand-blue:#245a8c;
  --brand-teal:#33a6d7;
  --brand-green:#9bcb3c;
  --text-grey:#6a6a6a;
  --hero-text:#55595d;
  --welcome-bg:#e2ebf1;
  --quote-bg:#f4f2f2;
  --footer-bg:#d0d1d2;
  --footer-text:#8b8d90;
  --bottom-bar:#a9aaab;
  --social-text:#5e6063;
  --divider:#e8e8ea;
}
*{margin:0;padding:0;box-sizing:border-box}
html,body{width:906px;height:1200px;overflow:hidden}
body{position:relative;font-family:"PT Sans",sans-serif;background:#fff;color:var(--text-grey)}
.abs{position:absolute}

/* hero */
.hero{left:0;top:0;width:906px;height:378px;
  background:
    linear-gradient(90deg,rgba(226,229,230,.78) 0%,rgba(218,222,223,.6) 30%,rgba(200,203,204,0) 55%),
    linear-gradient(180deg,#c9ced0 0%,#b3b8ba 25%,#9a968f 50%,#86796d 70%,#9a9690 100%)}
.hero-shore{left:0;top:300px;width:906px;height:78px;background:rgba(120,125,130,.3)}
.site-header{left:0;top:0;width:906px;height:55px;background:rgba(255,255,255,.85)}
.header-brand{left:88px;top:12px;display:flex;align-items:center;gap:5px;font-size:8px;letter-spacing:1.5px;color:var(--brand-blue)}
.dot{display:inline-block;border-radius:50%;background:var(--brand-blue)}
.header-name{left:178px;top:11px;font-size:12px;line-height:15px;color:#555;letter-spacing:.3px}
.main-nav{left:398px;top:19px;display:flex;font-size:11.5px;color:#4d4d4d;letter-spacing:.3px}
.main-nav a{color:inherit;text-decoration:none;position:relative;margin-right:22px}
.main-nav a.active::before{content:"";position:absolute;left:1px;right:1px;top:-19px;height:3px;background:var(--brand-teal)}
.hero-brand{left:56px;top:100px;text-align:center;width:280px;color:var(--hero-text)}
.hero-brand .dot{width:70px;height:70px;margin-bottom:22px}
.hero-brand .name{font-size:25px;letter-spacing:7px;display:block;line-height:30px}
.hero-brand .sub{font-size:12px;letter-spacing:5px;display:block;margin-top:7px;font-weight:700}

/* welcome */
.welcome{left:0;top:378px;width:906px;height:164px;background:var(--welcome-bg);text-align:center}
.welcome h1{font-weight:400;font-size:28px;letter-spacing:6.6px;color:#6d6d6d;margin-top:44px}
.welcome .rule{margin:10px auto 0;width:659px;height:5px;border-top:1px solid #8a9aa6;border-bottom:1px solid #8a9aa6}
.welcome p{font-size:13px;line-height:16px;color:#707274;margin-top:8px}

/* content */
.portrait{left:98px;top:573px;width:250px;height:366px;background:linear-gradient(160deg,#b8b8b8,#8d8d8d 55%,#4d4d4d)}
.section-title{font-size:15px;color:#333;font-weight:400;display:flex;align-items:center;gap:5px}
.section-title::after{content:"";flex:1;height:3px;border-top:1px solid #ddd;border-bottom:1px solid #ddd}
.services{left:436px;top:572px;width:297px}
.service-list{list-style:none;margin-top:14px}
.service-list li{display:flex;align-items:center;gap:8px;font-size:8px;color:#666;height:22px}
.service-list svg{flex:none}
.testimonials{left:434px;top:766px;width:296px}
.quote{margin:15px 0 0 3px;background:var(--quote-bg);padding:14px 16px;font-size:7.6px;line-height:13px;font-style:italic;color:#666;position:relative}
.quote::after{content:"";position:absolute;left:26px;bottom:-9px;border-left:12px solid var(--quote-bg);border-bottom:9px solid transparent}
.client{display:flex;align-items:center;gap:14px;margin:9px 0 0 3px;font-size:7.5px;font-weight:700;color:#444}

/* footer */
.footer-gap{left:0;top:966px;width:906px;height:8px;background:var(--divider)}
.site-footer{left:0;top:974px;width:906px;height:188px;background:var(--footer-bg);color:var(--footer-text)}
.footer-brand{left:172px;top:20px;width:144px;text-align:center;color:#7d8083}
.footer-brand .dot{width:40px;height:40px;margin-bottom:8px}
.footer-brand .name{display:block;font-size:12px;letter-spacing:3px}
.footer-brand .sub{display:block;font-size:7px;letter-spacing:3px;margin-top:2px}
.footer-about{left:178px;top:112px;width:140px;font-size:8px;line-height:13px;font-style:italic;font-weight:700;color:#7a7c7f}
.footer-h{font-size:16px;font-weight:400;letter-spacing:.5px}
.footer-contact{left:409px;top:17px;font-size:11px;line-height:17.5px}
.footer-contact .footer-h{margin-bottom:10px}
.footer-contact .gap{height:17px}
.footer-menu{left:655px;top:14px;font-size:13px;line-height:17.5px}
.footer-menu .footer-h{margin-bottom:8px}
.footer-menu a{display:block;color:inherit;text-decoration:none}
.bottom-bar{left:0;top:1162px;width:906px;height:38px;background:var(--bottom-bar)}
.copyright{left:149px;top:14px;font-size:7px;color:#fff}
.social{left:646px;top:12px;display:flex;gap:12px}
.social a{font-size:9px;font-weight:700;color:var(--social-text);text-decoration:none;letter-spacing:.3px}
</style>
</head>
<body>
  <div class="abs hero" role="img" aria-label="Calm photograph of a sandy beach with a rock, gentle waves and misty cliffs"></div>
  <div class="abs hero-shore"></div>

  <header class="abs site-header">
    <div class="abs header-brand"><span class="dot" style="width:10px;height:10px"></span>STILLBROOK</div>
    <div class="abs header-name">Colette Brannigan, LCSW,<br>Registered Play Therapist</div>
    <nav class="abs main-nav">
      <a class="active" href="#">HOME</a><a href="#">ABOUT ME</a><a href="#">COUNSELING SERVICES</a><a href="#">FEES</a><a href="#">FAQS</a><a href="#">CONTACT ME</a>
    </nav>
  </header>

  <div class="abs hero-brand">
    <span class="dot"></span>
    <span class="name">STILLBROOK</span>
    <span class="sub">COUNSELING</span>
  </div>

  <section class="abs welcome">
    <h1>WELCOME TO STILLBROOK COUNSELING</h1>
    <div class="rule"></div>
    <p>Lid est laborum dolo rumes fugats untras. Etharums ser quidem rerum<br>facilis dolores nemis omnis fugats vitaes nemo minima rerums unsers sadips amets.</p>
  </section>

  <div class="abs portrait" role="img" aria-label="Black and white portrait photograph of the therapist"></div>

  <section class="abs services">
    <h2 class="section-title">Services We Offer</h2>
    <ul class="service-list">
      <li><svg width="11" height="11" viewBox="0 0 11 11"><circle cx="5.5" cy="5.5" r="5.5" fill="#245a8c"/><path d="M4.5 3.2 6.8 5.5 4.5 7.8" stroke="#fff" stroke-width="1.4" fill="none"/></svg>Cras rutrum leo at odio volutpat id blandit fugiats ipsum ornare.</li>
      <li><svg width="11" height="11" viewBox="0 0 11 11"><circle cx="5.5" cy="5.5" r="5.5" fill="#245a8c"/><path d="M4.5 3.2 6.8 5.5 4.5 7.8" stroke="#fff" stroke-width="1.4" fill="none"/></svg>Donec fermentum porttitor nunc, sit amet gravida est porttitor vel.</li>
      <li><svg width="11" height="11" viewBox="0 0 11 11"><circle cx="5.5" cy="5.5" r="5.5" fill="#245a8c"/><path d="M4.5 3.2 6.8 5.5 4.5 7.8" stroke="#fff" stroke-width="1.4" fill="none"/></svg>Maecenas quis nisi in uctus adipiscing sed vehicula tellus amet dolore.</li>
      <li><svg width="11" height="11" viewBox="0 0 11 11"><circle cx="5.5" cy="5.5" r="5.5" fill="#245a8c"/><path d="M4.5 3.2 6.8 5.5 4.5 7.8" stroke="#fff" stroke-width="1.4" fill="none"/></svg>Aenean faucibus sapien a odio varius aliquet voluptas sadips..</li>
      <li><svg width="11" height="11" viewBox="0 0 11 11"><circle cx="5.5" cy="5.5" r="5.5" fill="#245a8c"/><path d="M4.5 3.2 6.8 5.5 4.5 7.8" stroke="#fff" stroke-width="1.4" fill="none"/></svg>Suspendisse venenatis euismod ve vestibulum volutpat nibh imperdiets.</li>
      <li><svg width="11" height="11" viewBox="0 0 11 11"><circle cx="5.5" cy="5.5" r="5.5" fill="#245a8c"/><path d="M4.5 3.2 6.8 5.5 4.5 7.8" stroke="#fff" stroke-width="1.4" fill="none"/></svg>Quisque non leo molestie augue imperdiet sollicitudin eu nec urna.</li>
    </ul>
  </section>

  <section class="abs testimonials">
    <h2 class="section-title">What Client’s Say</h2>
    <blockquote class="quote">“Neque porro quisquam est, qui dolorem ipsum quia dolor sit amet, consec tetur, adipisci velit, sed quia non numquam eius modi tempora incidunt utis labore et dolore magnam aliquam quaerat voluptatem. Ut enim ad minimas veniam, quis nostrum exercitationem ullam corporis suscipit laboriosam, nisi ut aliquid ex ea commodi consequatur slores amet untras vel illum qui.”</blockquote>
    <div class="client">
      <svg width="16" height="16" viewBox="0 0 16 16"><circle cx="8" cy="5" r="3.5" fill="#5b3b55"/><path d="M1 16c0-4 3-6 7-6s7 2 7 6z" fill="#5b3b55"/></svg>
      Jon Doe
    </div>
  </section>

  <div class="abs footer-gap"></div>
  <footer class="abs site-footer">
    <div class="abs footer-brand">
      <span class="dot"></span>
      <span class="name">STILLBROOK</span>
      <span class="sub">COUNSELING</span>
    </div>
    <p class="abs footer-about">Lorem ipsum ex vix illud nonummy, novum tation et his. At vix scriptaset patrioque scribentur, at pro fugit erts verterem molestiae, sed et vivendo ali Lorem ipsum ex vix illud</p>
    <div class="abs footer-contact">
      <h3 class="footer-h">CONTACT</h3>
      Colette Brannigan<br>2260 Alder Crest Road
      <div class="gap"></div>(208)555-0187
      <div class="gap"></div>colette@stillbrook.example
    </div>
    <nav class="abs footer-menu">
      <h3 class="footer-h">MENU</h3>
      <a href="#">HOME</a><a href="#">ABOUT ME</a><a href="#">COUNSELING SERVICES</a><a href="#">FEES</a><a href="#">FAQs</a><a href="#">CONTACT ME</a><a href="#">BLOG</a>
    </nav>
  </footer>
  <div class="abs bottom-bar">
    <p class="abs copyright">Copyright 2016 Stillbrook Counseling | All Rights Reserved</p>
    <nav class="abs social" aria-label="Social links"><a href="#">Share</a><a href="#">Follow</a><a href="#">Feed</a></nav>
  </div>
</body>
</html>
```